Celebration Cake brochure for boutique cake store

Looking for a cake brochure which displays the photo of the cake along with the description. Don't mind what style of brochure or size you do. We are a boutique bakery with both Italian and Australian cakes. I have a few ranges of products that I need to produce brochures (such as other sweets) but this is the first one required. *more photo to come

Industry/Entity Type

Bakery

Font styles to use
Sans Serif

Colors

Designer to choose colors to be used in the design.

Requirements
Must have
• Easy for customers to use the brochure to choose their cake. Don't mind what size brochure/menu you use

```html
<!DOCTYPE html>
<html lang="en">
<head>
<meta charset="utf-8">
<title>Celebration Cakes Brochure Spread</title>
<link rel="stylesheet" href="https://fonts.googleapis.com/css2?family=Cinzel:wght@600&family=Montserrat:wght@500&display=swap">
<style>
  :root {
    --backdrop: #e9e4dc;
    --paper: #f7f7f7;
    --rule: #a3203b;
    --badge-red: #9e1b34;
    --gold: #c9a838;
    --gold-soft: #e3cf86;
    --ink: #2b2b2b;
    --choc-dark: #3d2416;
    --choc-mid: #6e4630;
    --cream-light: #efe3bd;
    --cream-mid: #c9b27a;
    --wood: #5a3a22;
  }
  * { box-sizing: border-box; margin: 0; padding: 0; }
  html, body {
    width: 1200px; height: 481px; overflow: hidden;
    background: var(--backdrop);
  }
  .spread {
    position: absolute; left: 40px; top: 20px;
    width: 1120px; height: 441px;
    display: flex;
    box-shadow: 0 6px 18px rgba(0,0,0,0.18);
  }
  .page {
    width: 560px; height: 100%;
    display: grid;
    grid-template-columns: 1fr 1fr;
    grid-template-rows: 1fr 1fr;
    gap: 1px;
    background: var(--rule);
  }
  .page--left { border-right: 1px solid #d8d8d8; }
  .cell {
    background: var(--paper);
    display: flex; flex-direction: column;
    align-items: center; justify-content: center;
    padding: 14px 18px;
    min-width: 0;
  }
  .cell--photo { padding: 6px; }
  .cake-photo { width: 100%; height: 100%; }
  .cake-photo--dark {
    background: radial-gradient(ellipse at 50% 45%, var(--choc-mid) 0%, var(--choc-dark) 55%, var(--wood) 100%);
  }
  .cake-photo--white {
    background: radial-gradient(ellipse at 50% 50%, var(--cream-light) 0%, var(--cream-mid) 55%, var(--wood) 100%);
  }
  .cake-title {
    display: flex; align-items: center; gap: 8px;
    margin-bottom: 26px;
  }
  .title-badge {
    font-family: "Cinzel", serif; font-weight: 600;
    font-size: 15px; letter-spacing: 0.5px;
    color: #fff; background: var(--badge-red);
    border: 2px solid var(--gold);
    border-radius: 12px;
    padding: 3px 14px 4px;
    white-space: nowrap;
  }
  .ornament {
    width: 34px; height: 8px;
    border-radius: 4px;
    background: linear-gradient(90deg, var(--gold-soft), var(--gold));
  }
  .ornament--right {
    background: linear-gradient(90deg, var(--gold), var(--gold-soft));
  }
  .cake-desc {
    font-family: "Montserrat", sans-serif; font-weight: 500;
    font-size: 10.5px; line-height: 1.3;
    color: var(--ink); text-align: center;
    max-width: 170px;
  }
</style>
</head>
<body>
<main class="spread">
  <section class="page page--left">
    <div class="cell cell--photo"><div class="cake-photo cake-photo--dark" role="img" aria-label="Photo of the Colle Scuro cake topped with folded dark chocolate sheets"></div></div>
    <div class="cell">
      <div class="cake-title">
        <span class="ornament" role="img" aria-label="Gold scroll ornament"></span>
        <h2 class="title-badge">Colle Scuro</h2>
        <span class="ornament ornament--right" role="img" aria-label="Gold scroll ornament"></span>
      </div>
      <p class="cake-desc">Arancello chocolate chantilly cream with vanilla sponge surrounded with sponge crumb &amp; topped with a mound of chocolate.</p>
    </div>
    <div class="cell">
      <div class="cake-title">
        <span class="ornament" role="img" aria-label="Gold scroll ornament"></span>
        <h2 class="title-badge">Colle Chiaro</h2>
        <span class="ornament ornament--right" role="img" aria-label="Gold scroll ornament"></span>
      </div>
      <p class="cake-desc">Arancello chantilly cream with vanilla sponge surrounded with sponge crumb &amp; topped with a mound of white chocolate.</p>
    </div>
    <div class="cell cell--photo"><div class="cake-photo cake-photo--white" role="img" aria-label="Photo of the Colle Chiaro cake topped with folded white chocolate sheets"></div></div>
  </section>
  <section class="page page--right">
    <div class="cell cell--photo"><div class="cake-photo cake-photo--dark" role="img" aria-label="Photo of the Colle Scuro cake topped with folded dark chocolate sheets"></div></div>
    <div class="cell">
      <div class="cake-title">
        <span class="ornament" role="img" aria-label="Gold scroll ornament"></span>
        <h2 class="title-badge">Colle Scuro</h2>
        <span class="ornament ornament--right" role="img" aria-label="Gold scroll ornament"></span>
      </div>
      <p class="cake-desc">Arancello chocolate chantilly cream with vanilla sponge surrounded with sponge crumb &amp; topped with a mound of chocolate.</p>
    </div>
    <div class="cell">
      <div class="cake-title">
        <span class="ornament" role="img" aria-label="Gold scroll ornament"></span>
        <h2 class="title-badge">Colle Chiaro</h2>
        <span class="ornament ornament--right" role="img" aria-label="Gold scroll ornament"></span>
      </div>
      <p class="cake-desc">Arancello chantilly cream with vanilla sponge surrounded with sponge crumb &amp; topped with a mound of white chocolate.</p>
    </div>
    <div class="cell cell--photo"><div class="cake-photo cake-photo--white" role="img" aria-label="Photo of the Colle Chiaro cake topped with folded white chocolate sheets"></div></div>
  </section>
</main>
</body>
</html>
```